New florist business website design

Number 1 want is an easy to navigate & check out website
Needs to be beautiful and eye catching as well.
This is an online only business (no shop front)
Rustic and blush pinks, neutrals, woods, leaves
Customers need to be able to go onto my website, select something they want to buy but have the option to use a drop down box to change colours of the flowers, or add notes to make changes to the arrangement

Industry/Entity Type

Florist

Coding

Coded - Design and coding required

Number of Pages Required

5+ page

Colors
f9d9e8
fff2ec
fffefc

Requirements
Must have
• Drop down menu to take you to other pages for Arrangements, bouquets, everlasting arrangements, gifts, contact
Be able to purchase and “add to basket”
Checkout page
Nice to have
• Be able to add my own photos once I’ve taken new ones
Should not have
• Tacky images or clip art

```html
<!DOCTYPE html>
<html lang="en">
<head>
<meta charset="utf-8">
<title>Fern &amp; Bloom — Florist</title>
<link rel="stylesheet" href="https://fonts.googleapis.com/css2?family=Playfair+Display:wght@400;700;900&family=Roboto:wght@400;500;700&family=Great+Vibes&display=swap">
<style>
:root{
  --blush:#f9d9e8;
  --cream:#fff2ec;
  --paper:#fffefc;
  --pink:#e8569a;
  --ink:#1c1c1c;
  --muted:#555;
  --gold:#f2b400;
  --line:#e6e6e6;
}
*{box-sizing:border-box;margin:0;padding:0}
html,body{width:1200px;height:4605px;overflow:hidden;background:var(--paper);color:var(--ink);font-family:"Roboto",Arial,sans-serif}
.page{position:relative;width:1200px;height:4605px}
.ph{display:block}
/* top bar */
.topbar{position:absolute;top:0;left:0;width:1200px;height:40px;background:var(--cream);font-size:13px;font-weight:500}
.topbar .ship{position:absolute;left:98px;top:12px;display:flex;gap:8px;align-items:center}
.topbar .utils{position:absolute;right:50px;top:12px;display:flex;gap:36px}
.topbar .utils span{display:flex;gap:6px;align-items:center}
/* nav */
.nav{position:absolute;top:40px;left:0;width:1200px;height:103px;display:flex;align-items:center;font-family:"Playfair Display",serif;font-size:15px;color:#333}
.nav .menu{position:absolute;top:40px;display:flex;gap:36px}
.nav .menu.left{left:160px}
.nav .menu.right{left:698px}
.caret{font-size:10px;margin-left:3px}
.brand{position:absolute;left:540px;top:22px;width:120px;height:60px;display:flex;align-items:center;justify-content:center;gap:6px;font-family:"Playfair Display",serif;font-size:18px;color:#666}
.brand i{width:8px;height:8px;border-radius:50%;background:var(--blush);display:block}
/* hero */
.hero{position:absolute;top:143px;left:0;width:1200px;height:585px;background:linear-gradient(100deg,#dfe6ee 0%,#cbd8e4 30%,#e9eef3 48%,#f4c7cf 62%,#ef9fac 78%,#f7d7d9 100%)}
.hero h1{position:absolute;left:100px;top:98px;font-family:"Playfair Display",serif;font-weight:900;font-size:72px;line-height:70px;color:#111;letter-spacing:-0.5px}
.btn{display:inline-flex;align-items:center;justify-content:center;background:var(--pink);color:#fff;font-family:"Playfair Display",serif;font-weight:700;font-size:14px}
.hero .btn{position:absolute;left:98px;top:331px;width:145px;height:44px}
/* section headings */
.kicker{position:absolute;left:0;width:1200px;text-align:center;font-size:21px;color:#333}
.title{position:absolute;left:0;width:1200px;text-align:center;font-family:"Playfair Display",serif;font-size:45px;color:#111}
.lead{position:absolute;left:250px;width:700px;text-align:center;font-size:14px;line-height:26px;color:#222}
/* occasions */
.occ{position:absolute;width:238px;height:309px}
.occ .ph{width:238px;height:263px}
.occ .label{height:46px;background:var(--blush);display:flex;align-items:center;justify-content:center;font-size:18px;font-weight:500;letter-spacing:0.3px}
/* join */
.join{position:absolute;top:1725px;left:0;width:1200px;height:305px;background:var(--cream)}
.field{position:absolute;top:190px;height:46px;width:318px;background:#fff;font-size:13px;padding:16px 18px;color:#222}
.join .btn{position:absolute;left:855px;top:190px;width:146px;height:46px;font-size:16px}
/* products */
.card{position:absolute;width:238px;height:318px;background:#fff;box-shadow:0 0 8px rgba(0,0,0,.12);text-align:center}
.card .ph{position:absolute;left:6px;top:6px;width:226px;height:178px;background:#f2f2f2}
.card .ph div{position:absolute;left:63px;top:14px;width:100px;height:150px;border-radius:50px 50px 20px 20px}
.card .name{position:absolute;top:198px;width:100%;font-size:13px;color:#222}
.stars{color:var(--gold);font-size:12px;letter-spacing:1px}
.card .stars{position:absolute;top:218px;width:100%}
.card .price{position:absolute;top:243px;width:100%;font-family:"Playfair Display",serif;font-size:15px}
.card .ctrl{position:absolute;left:6px;top:279px;width:226px;height:34px;display:flex;gap:4px}
.choose{width:118px;height:34px;border:1px solid var(--line);display:flex;align-items:center;padding-left:6px;font-size:9px;color:#555;gap:8px}
.choose b{width:16px;height:16px;background:#f00;display:block;margin-left:auto}
.choose em{font-style:normal;font-size:8px;margin-right:4px}
.card .add{flex:1;background:var(--blush);display:flex;align-items:center;justify-content:center;font-family:"Playfair Display",serif;font-weight:700;font-size:12px;color:#333}
/* deal */
.deal{position:absolute;top:2954px;left:0;width:1200px;height:399px;background:linear-gradient(90deg,#f6d4d8 0%,#fbe5e6 30%,#fde9ea 70%,#f6d2d6 100%)}
.deal .flowers-l{position:absolute;left:0;top:0;width:390px;height:399px;background:radial-gradient(circle at 40% 45%,#f07e98 0%,#f3a8b6 35%,#8ca46c 65%,rgba(250,225,228,0) 80%)}
.deal .flowers-r{position:absolute;right:0;top:30px;width:230px;height:369px;background:radial-gradient(circle at 65% 55%,#ee8aa2 0%,#f5b7c3 40%,#7e9b60 62%,rgba(250,225,228,0) 80%)}
.deal .script{position:absolute;left:0;top:65px;width:1200px;text-align:center;font-family:"Great Vibes",cursive;font-size:52px;color:#222}
.deal .sub{position:absolute;left:0;top:130px;width:1200px;text-align:center;font-family:"Playfair Display",serif;font-size:30px;color:#222}
.deal .off{position:absolute;left:0;top:185px;width:1200px;text-align:center;font-family:"Playfair Display",serif;font-size:52px;color:#111}
.deal .btn{position:absolute;left:609px;top:282px;width:144px;height:44px}
/* testimonials */
.testi{position:absolute;width:240px;text-align:center}
.testi .ph{width:240px;height:273px}
.testi .who{margin-top:16px;font-size:16px;font-weight:700}
.testi .stars{margin-top:6px;font-size:14px}
.testi p{margin-top:6px;font-size:11px;font-style:italic;line-height:19px;color:#333}
/* footer */
.footer{position:absolute;top:4036px;left:0;width:1200px;height:262px;background:var(--cream)}
.fcol{position:absolute;top:46px;width:240px;text-align:center}
.fcol h4{display:inline-block;font-size:19px;font-weight:700;border-bottom:2px solid #222;padding-bottom:2px;margin-bottom:12px}
.fcol li{list-style:none;font-size:14px;line-height:26px;color:#222}
.social{position:absolute;left:502px;top:198px;display:flex;gap:6px}
.social i{width:30px;height:30px;border-radius:50%;background:#222;display:block}
/* gallery */
.gallery{position:absolute;top:4298px;left:0;width:1200px;height:238px;display:flex}
.gallery .ph{width:200px;height:238px}
.gallery .dot{position:absolute;left:566px;top:8px;width:26px;height:26px;border:2px solid #fff;border-radius:7px}
.copy{position:absolute;top:4536px;left:0;width:1200px;height:69px;display:flex;align-items:center;justify-content:center;font-size:14px;color:#333;background:var(--paper)}
</style>
</head>
<body>
<div class="page">

  <div class="topbar">
    <div class="ship">
      <svg width="22" height="14" viewBox="0 0 22 14" fill="none" stroke="#222" stroke-width="1.4"><rect x="1" y="1" width="13" height="9"/><path d="M14 4h4l3 3v3h-7"/><circle cx="5" cy="11.5" r="1.6" fill="#fff"/><circle cx="17" cy="11.5" r="1.6" fill="#fff"/></svg>
      Complimentary Shipping On domestic orders over $50
    </div>
    <div class="utils">
      <span><svg width="12" height="13" viewBox="0 0 12 13" fill="none" stroke="#222" stroke-width="1.3"><circle cx="6" cy="4" r="3"/><path d="M1 12c0-3 2.2-4.5 5-4.5S11 9 11 12"/></svg>MY ACCOUNT</span>
      <span><svg width="13" height="13" viewBox="0 0 13 13" fill="none" stroke="#222" stroke-width="1.3"><path d="M2 4h9l-1 8H3z"/><path d="M4.5 4V2.5a2 2 0 0 1 4 0V4"/></svg>CART</span>
      <span><svg width="13" height="13" viewBox="0 0 13 13" fill="none" stroke="#222" stroke-width="1.3"><circle cx="7.5" cy="5.5" r="4"/><path d="M4.5 8.5L1 12"/></svg>SEARCH</span>
    </div>
  </div>

  <nav class="nav">
    <div class="menu left"><span>Home<span class="caret">▾</span></span><span>Arrangements<span class="caret">▾</span></span><span>Bouquets<span class="caret">▾</span></span></div>
    <div class="brand"><i></i>Fern &amp; Bloom</div>
    <div class="menu right"><span>Everlasting arrangements<span class="caret">▾</span></span><span>Gifts<span class="caret">▾</span></span><span>Contact</span></div>
  </nav>

  <header class="hero" role="img" aria-label="Photo of a pink rose and wildflower arrangement in a wicker basket on a snowy background">
    <h1>Live in<br>moments<br>that matter.</h1>
    <a class="btn">Shop Now</a>
  </header>

  <section class="occasions">
    <div class="kicker" style="top:792px">Roses, Flowers, Plants &amp; Gifts To</div>
    <h2 class="title" style="top:825px">Shop Our Occasion</h2>
    <p class="lead" style="top:886px">Lorem ipsum dolor sit amet, consectetur adipiscing elit, sed do eiusmod tempor incididunt ut labore et dolore magna aliqua. Quis ipsum suspendisse ultrices gravida. Risus commodo viverra maecenas accumsan lacus vel facilisis.</p>

    <div class="occ" style="left:98px;top:998px"><div class="ph" role="img" aria-label="Photo of a sympathy wreath of roses" style="background:radial-gradient(circle,#6a7a4a 0 25%,#e7a7a6 40%,#9bb27a 55%,#4d4a3e 75%)"></div><div class="label">SYMPATHY</div></div>
    <div class="occ" style="left:352px;top:998px"><div class="ph" role="img" aria-label="Photo of a birthday flower box with yellow roses and macarons" style="background:radial-gradient(circle at 50% 40%,#f2cf3a 0 22%,#c8a0c8 38%,#f3e7e6 55%,#b08a6d 85%)"></div><div class="label">BIRTHDAY</div></div>
    <div class="occ" style="left:606px;top:998px"><div class="ph" role="img" aria-label="Photo of a red rose bouquet" style="background:radial-gradient(circle,#a0101e 0 30%,#c23242 50%,#6a1414 80%)"></div><div class="label">LOVE &amp; ROMANCE</div></div>
    <div class="occ" style="left:860px;top:998px"><div class="ph" role="img" aria-label="Photo of a white hydrangea anniversary bouquet" style="background:radial-gradient(circle at 50% 35%,#f3ebe4 0 25%,#d9b9ba 45%,#4a3a30 80%)"></div><div class="label">ANNIVERSARY</div></div>

    <div class="occ" style="left:98px;top:1325px"><div class="ph" role="img" aria-label="Photo of a lilac new baby bouquet with balloons" style="background:linear-gradient(160deg,#b9a2cf,#e9dcef 45%,#c9a0c6 75%,#e8e2ea)"></div><div class="label">NEW BABY</div></div>
    <div class="occ" style="left:352px;top:1325px"><div class="ph" role="img" aria-label="Photo of white roses in a gold vase" style="background:linear-gradient(180deg,#f5f3ec 0 45%,#c9ac52 60%,#8a6e26 100%)"></div><div class="label">CONGRATULATIONS</div></div>
    <div class="occ" style="left:606px;top:1325px"><div class="ph" role="img" aria-label="Photo of a mixed pink and burgundy thank-you bouquet" style="background:radial-gradient(circle at 50% 40%,#e6a8b4 0 25%,#8e2a4a 45%,#dfe2e4 70%)"></div><div class="label">THANKS</div></div>
    <div class="occ" style="left:860px;top:1325px"><div class="ph" role="img" aria-label="Photo of a get-well bouquet wrapped in pink paper" style="background:radial-gradient(circle at 45% 40%,#f08a6a 0 20%,#e4475e 38%,#f3c7d3 60%,#eee 85%)"></div><div class="label">GETWELL</div></div>
  </section>

  <section class="join">
    <h2 class="title" style="top:58px;font-size:38px">Join the Fern &amp; Bloom</h2>
    <p class="lead" style="top:118px">Lorem ipsum dolor sit amet, consectetur adipiscing elit, sed do eiusmod tempor incididunt ut labore et dolore magna aliqua. Quis ipsum suspendisse ultrices gravida.</p>
    <div class="field" style="left:197px">Full Name</div>
    <div class="field" style="left:526px">Email Address</div>
    <a class="btn">Sign Up!</a>
  </section>

  <section class="featured">
    <div class="kicker" style="top:2096px">Roses, Flowers, Plants &amp; Gifts To</div>
    <h2 class="title" style="top:2128px">Featured Products</h2>

    <div class="card" style="left:98px;top:2212px"><div class="ph" role="img" aria-label="Photo of lilies and roses in a red vase"><div style="background:radial-gradient(circle at 50% 30%,#e8442e 0 30%,#f29a3b 50%,#6f9c4a 75%)"></div></div><div class="name">SPRING FLING TULIP VASE</div><div class="stars">★★★★★</div><div class="price">$ 49.99</div><div class="ctrl"><div class="choose">Choose Color<b></b><em>▾</em></div><div class="add">Add To Cart</div></div></div>
    <div class="card" style="left:352px;top:2212px"><div class="ph" role="img" aria-label="Photo of pink roses in a glass cube"><div style="background:radial-gradient(circle at 50% 35%,#e8559a 0 30%,#c98ad0 50%,#7ca55a 75%)"></div></div><div class="name">SPRING FLING TULIP VASE</div><div class="stars">★★★★★</div><div class="price">$ 49.99</div><div class="ctrl"><div class="choose">Choose Color<b></b><em>▾</em></div><div class="add">Add To Cart</div></div></div>
    <div class="card" style="left:606px;top:2212px"><div class="ph" role="img" aria-label="Photo of a white and pink flower basket"><div style="background:radial-gradient(circle at 50% 45%,#f4f0e6 0 30%,#f2b7cc 50%,#b6c98a 75%)"></div></div><div class="name">SPRING FLING TULIP VASE</div><div class="stars">★★★★★</div><div class="price">$ 49.99</div><div class="ctrl"><div class="choose">Choose Color<b></b><em>▾</em></div><div class="add">Add To Cart</div></div></div>
    <div class="card" style="left:860px;top:2212px"><div class="ph" role="img" aria-label="Photo of mixed tulips in a vase"><div style="background:radial-gradient(circle at 50% 30%,#e53a4c 0 20%,#f0c23a 38%,#8a5bc8 52%,#5f9a4a 75%)"></div></div><div class="name">SPRING FLING TULIP VASE</div><div class="stars">★★★★★</div><div class="price">$ 49.99</div><div class="ctrl"><div class="choose">Choose Color<b></b><em>▾</em></div><div class="add">Add To Cart</div></div></div>

    <div class="card" style="left:98px;top:2544px"><div class="ph" role="img" aria-label="Photo of green and yellow lilies in a vase"><div style="background:radial-gradient(circle at 50% 30%,#d9df4a 0 28%,#7fb24a 55%,#c7e0d2 80%)"></div></div><div class="name">SPRING FLING TULIP VASE</div><div class="stars">★★★★★</div><div class="price">$ 49.99</div><div class="ctrl"><div class="choose">Choose Color<b></b><em>▾</em></div><div class="add">Add To Cart</div></div></div>
    <div class="card" style="left:352px;top:2544px"><div class="ph" role="img" aria-label="Photo of orange and white roses in a vase"><div style="background:radial-gradient(circle at 50% 30%,#f08a3a 0 28%,#f6f0e6 48%,#6f9a4a 75%)"></div></div><div class="name">SPRING FLING TULIP VASE</div><div class="stars">★★★★★</div><div class="price">$ 49.99</div><div class="ctrl"><div class="choose">Choose Color<b></b><em>▾</em></div><div class="add">Add To Cart</div></div></div>
    <div class="card" style="left:606px;top:2544px"><div class="ph" role="img" aria-label="Photo of purple and magenta flowers in a red vase"><div style="background:radial-gradient(circle at 50% 30%,#6a2a9a 0 28%,#c0245e 50%,#5f8a42 75%)"></div></div><div class="name">SPRING FLING TULIP VASE</div><div class="stars">★★★★★</div><div class="price">$ 49.99</div><div class="ctrl"><div class="choose">Choose Color<b></b><em>▾</em></div><div class="add">Add To Cart</div></div></div>
    <div class="card" style="left:860px;top:2544px"><div class="ph" role="img" aria-label="Photo of purple iris and pink lilies in a vase"><div style="background:radial-gradient(circle at 50% 30%,#7a5ac8 0 28%,#e28ab8 48%,#6f9a4a 75%)"></div></div><div class="name">SPRING FLING TULIP VASE</div><div class="stars">★★★★★</div><div class="price">$ 49.99</div><div class="ctrl"><div class="choose">Choose Color<b></b><em>▾</em></div><div class="add">Add To Cart</div></div></div>
  </section>

  <section class="deal">
    <div class="flowers-l" role="img" aria-label="Photo of pink roses and white blossoms"></div>
    <div class="flowers-r" role="img" aria-label="Photo of pink roses with green leaves"></div>
    <div class="script">Deal of the day</div>
    <div class="sub">Standard Lorem Ipsum sage, used</div>
    <div class="off">50% Off</div>
    <a class="btn">Shop Now</a>
  </section>

  <section class="testimonials">
    <div class="kicker" style="top:3434px">Roses, Flowers, Plants &amp; Gifts To</div>
    <h2 class="title" style="top:3466px">Client Testimonials</h2>

    <div class="testi" style="left:98px;top:3553px"><div class="ph" role="img" aria-label="Photo of two customers wearing flower crowns" style="background:linear-gradient(180deg,#5d6a42,#b89a7c 45%,#7a3a46 80%)"></div><div class="who">JOHN SMITH</div><div class="stars">★★★★★</div><p>"Lorem ipsum dolor sit amet, ctur adipiscing elit, sed do eiusmod tempor incididunt ut labore et dolore magna aliqua"</p></div>
    <div class="testi" style="left:352px;top:3553px"><div class="ph" role="img" aria-label="Photo of pink roses in a white vase" style="background:linear-gradient(180deg,#ece8e4,#c89aaf 45%,#e6e2de 85%)"></div><div class="who">JOHN SMITH</div><div class="stars">★★★★★</div><p>"Lorem ipsum dolor sit amet, ctur adipiscing elit, sed do eiusmod tempor incididunt ut labore et dolore magna aliqua"</p></div>
    <div class="testi" style="left:606px;top:3553px"><div class="ph" role="img" aria-label="Photo of a customer holding a box of flowers outdoors" style="background:linear-gradient(180deg,#5a7046,#e7cfc4 40%,#2c2c2c 75%)"></div><div class="who">JOHN SMITH</div><div class="stars">★★★★★</div><p>"Lorem ipsum dolor sit amet, ctur adipiscing elit, sed do eiusmod tempor incididunt ut labore et dolore magna aliqua"</p></div>
    <div class="testi" style="left:860px;top:3553px"><div class="ph" role="img" aria-label="Photo of a red and pink bridal bouquet" style="background:radial-gradient(circle at 50% 40%,#c01e36 0 28%,#e8a0b0 48%,#f2efec 75%)"></div><div class="who">JOHN SMITH</div><div class="stars">★★★★★</div><p>"Lorem ipsum dolor sit amet, ctur adipiscing elit, sed do eiusmod tempor incididunt ut labore et dolore magna aliqua"</p></div>
  </section>

  <footer class="footer">
    <div class="fcol" style="left:80px"><h4>ABOUT</h4><ul><li>Our Story</li><li>Brands</li><li>Shop</li><li>About US</li></ul></div>
    <div class="fcol" style="left:452px"><h4>SUPPORT</h4><ul><li>FAQ</li><li>Contact Us</li><li>Press</li></ul></div>
    <div class="fcol" style="left:849px"><h4>INFO</h4><ul><li>Privacy Policy</li><li>Terms Of Services</li><li>Track Order</li><li>Join Us</li></ul></div>
    <div class="social" aria-label="Social links"><i></i><i></i><i></i><i></i></div>
  </footer>

  <div class="gallery">
    <div class="ph" role="img" aria-label="Photo of white roses in a dark basket" style="background:radial-gradient(circle,#d8dcd6 0 25%,#3a4a50 70%)"></div>
    <div class="ph" role="img" aria-label="Photo of red flowers and greenery" style="background:radial-gradient(circle,#d23a3a 0 25%,#5a7a46 60%,#e8e4e0)"></div>
    <div class="ph" role="img" aria-label="Photo of dusty pink roses" style="background:radial-gradient(circle,#b4505a 0 30%,#4a2e30 75%)"></div>
    <div class="ph" role="img" aria-label="Photo of two customers with flower crowns" style="background:linear-gradient(180deg,#5f6e48,#c49a86 50%,#2a2a2a)"></div>
    <div class="ph" role="img" aria-label="Photo of mauve and peach roses" style="background:radial-gradient(circle,#c99aa0 0 30%,#6f7a6a 75%)"></div>
    <div class="ph" role="img" aria-label="Photo of a red and orange bouquet in a jar" style="background:radial-gradient(circle,#e4583a 0 25%,#f2c0b0 50%,#eeeae6 80%)"></div>
    <span class="dot"></span>
  </div>

  <div class="copy">Copyright © 2021 Fern &amp; Bloom. All rights reserved.</div>
</div>
</body>
</html>
```